Wine label for new boutique South African wine focused on the USA market.

Wine label required for new ethical south African red wine called PLUMB which stands for 'Marlowe, tolland, brightly and you' but is also a play on 'SA' and that it has a story to tell. Gerald Marlowe is the wine maker, Tolland the farm owner, and Brightly an investor.

Concept is a simple old type writer font on a white/off white label. Front label would say 'Plumb No.1, 2010 Shiraz, South Africa' and similarly a second for another wine 'Plumb No.2, 2010 Cab/Merlot Blend. Maybe the round stain of the bottom of a wine bottle in the bottom corner? Would also like for the 'plumb' to double up as the logo and work in the form of a stamp.

The rear label will need to tell a short story and be able to accommodate the usual boilerplate info. The story will go something like, ' Plumb No.1: It's a long story, but in short we love our wine and we think you will too. The cooling see breezes of the Indian Ocean help define this world class Shiraz from the Western Cape. Aged in french oak for 20 months, the bold flavors will compliment all red meats or simply enjoy on its own. Learn more about our story at www.plumbvintners.example.

The cab/merlot will read similar: Plumb No.2: It's a long story, but in short we love our wine and we think you will too. The cooling see breezes of the Indian Ocean help define this world class red blend from the Western Cape. Aged in french oak for 20 months, this wine will compliment all red meats or simply enjoy on its own. Learn more about our story at www.plumbvintners.example.

Reason: Had some great designs already, but as i get to understand how ArtBazaarly works, I'm keen to explore as many ideas as possible. Neil

Thanks for all the great designs everybody!

We will make a tough decision in the next couple of days.

Regards

Neil

Target Market(s)

Middle class with some wine knowledge. Price point around $20 -30

Industry/Entity Type

Boutique

Requirements
Nice to have
• A small nod to the wine coming from south Africa in the design would be nice but nothing to over the top
Should not have
• Simple and clear font with plenty of empty space on the label

```html
<!DOCTYPE html>
<html lang="en">
<head>
<meta charset="utf-8">
<title>Plumb No.1 – Rear Label</title>
<link rel="stylesheet" href="https://fonts.googleapis.com/css2?family=Cutive&display=swap">
<style>
  :root {
    --paper: #ecebe6;
    --paper-light: #f3f2ee;
    --paper-shade: #e4e3dd;
    --ink: #161616;
  }
  html, body {
    margin: 0;
    padding: 0;
    width: 1200px;
    height: 1000px;
    overflow: hidden;
    background: var(--paper);
  }
  .label {
    position: relative;
    width: 1200px;
    height: 1000px;
    background:
      radial-gradient(ellipse at 50% 40%, var(--paper-light) 0%, var(--paper) 60%, var(--paper-shade) 100%);
    color: var(--ink);
    font-family: "Cutive", "Courier New", serif;
  }
  .brand {
    position: absolute;
    left: 0;
    right: 0;
    top: 272px;
    margin: 0;
    text-align: center;
    font-family: "Cutive", "Courier New", serif;
    font-weight: 400;
    font-size: 78px;
    line-height: 96px;
    color: var(--ink);
    padding-left: 24px;
  }
  .story {
    position: absolute;
    left: 100px;
    top: 645px;
    margin: 0;
    font-size: 23.6px;
    line-height: 35px;
    white-space: nowrap;
  }
  .story__link {
    position: absolute;
    left: 100px;
    top: 822px;
    margin: 0;
    font-size: 28px;
    line-height: 38px;
    white-space: nowrap;
  }
</style>
</head>
<body>
  <main class="label">
    <h1 class="brand">Plumb No.1</h1>
    <p class="story">
      It's a long story, but in short we love our wine and we think you will too.<br>
      The cooling sea breezes of the Indian Ocean help define this world class<br>
      Shiraz from the Western Cape. Aged in french oak for 20 months, the<br>
      bold flavors will compliment all red meats or simply enjoy on its own.
    </p>
    <p class="story__link">Learn more about our story at www.plumbvintners.example.</p>
  </main>
</body>
</html>
```